Yoga Workshop - Yoga Practice information flyer

I am a yoga teacher who will be presenting a workshop on yoga for sleep and need a brochure for my clients which outlines a practice that I give them so they can do the practice at home. Ideally I would like a brochure that is a single A3 size of paper in size that folds in half to an A4 booklet with the entire practice on the centre section to make it easy for people to do the practice at home with just one open page in front of them:
* Front page detailing "Yoga for Sleep Workshop" and "Restorative Yoga Practice"
* Centre contains the information on the practice contained in the attached word document. The practice consists of 5 postures, so there needs to be five separate sections which have the pictures of the postures (attached in uploaded files) and the wording contained in the attached word document. All pictures uploaded need to be included in the flyer as each posture has different pictures demonstrating the posture using yoga props or using things people have at home
* Back page containing a picture of myself (picture uploaded in files) with some information about me (contained in the attached word document) and my website www.lumaverisk.com.au

I also need this flyer to be able to printed on 2 double sided A4 sheets of paper so will require 2 x pdf file versions. Importantly, for the centre section of the flyer, the design needs to ensure if it is printed on A4 paper, the wording and pictures for each of the postures are not separated over two pages

Target Market(s)

Existing clients

Requirements
Must have
• Detailed in project description
Nice to have
• The word document also contains some quotes. These do not need to be included in the flyer. If there is room and there is room for one or two of those please include where it would look good
Should not have
• Stock pictures of people in yoga postures which a normal everyday person could not get into

```html
<!DOCTYPE html>
<html lang="en">
<head>
<meta charset="utf-8">
<title>Yoga for Sleep Workshop – Brochure</title>
<link rel="stylesheet" href="https://fonts.googleapis.com/css2?family=Montserrat:ital,wght@0,400;0,500;0,600;0,700;0,800;1,400;1,600;1,700&display=swap">
<style>
  :root {
    --stage: #9b9b9b;
    --navy: #1d2c49;
    --navy-deep: #15213a;
    --navy-band: #22355a;
    --copper: #d97c4c;
    --copper-deep: #b9683f;
    --paper: #f5f4f2;
    --ink: #24304b;
    --white: #ffffff;
    --mat: #1f74c4;
  }
  * { box-sizing: border-box; margin: 0; padding: 0; }
  html, body { width: 857px; height: 1200px; overflow: hidden; }
  body {
    background: var(--stage);
    font-family: "Montserrat", Arial, sans-serif;
    color: var(--ink);
    position: relative;
  }
  .spread {
    position: absolute;
    left: 20px;
    width: 817px;
    height: 578px;
    overflow: hidden;
    box-shadow: 0 6px 18px rgba(0,0,0,.25);
  }
  .spread--outer { top: 14px; display: flex; }
  .spread--inner { top: 608px; background: var(--navy); }

  /* ---------- back page ---------- */
  .back-page {
    width: 408.5px; height: 100%;
    background: radial-gradient(ellipse at 30% 60%, #21325a 0%, var(--navy) 55%, var(--navy-deep) 100%);
    color: var(--white);
    padding: 44px 34px 0;
    position: relative;
    text-align: center;
  }
  .back-page__title {
    color: var(--copper);
    font-style: italic;
    font-weight: 700;
    font-size: 17px;
    margin-bottom: 12px;
  }
  .back-page__bio {
    font-size: 7.6px;
    line-height: 1.45;
    font-style: italic;
    text-align: left;
  }
  .quote { margin-top: 22px; font-size: 8.4px; font-style: italic; line-height: 1.45; }
  .quote__mark {
    display: block;
    color: var(--copper);
    font-size: 26px;
    font-weight: 700;
    line-height: .6;
    height: 14px;
    font-style: italic;
  }
  .quote__source { display: block; }
  .back-page__web {
    position: absolute;
    left: 40px; bottom: 34px;
    font-size: 12px;
    letter-spacing: .5px;
  }

  /* ---------- front page ---------- */
  .front-page {
    width: 408.5px; height: 100%;
    position: relative;
    background: var(--navy-band);
  }
  .front-page__photo {
    position: absolute; inset: 0 0 148px 0;
    background: linear-gradient(180deg, #dfe3e6 0%, #cfd6d4 22%, #5c8a3a 38%, #3f6f2a 52%, #8f8a5c 70%, #a59670 100%);
  }
  .brand {
    position: absolute; top: 58px; left: 170px;
    text-align: center; width: 200px;
  }
  .brand__dot {
    display: block; width: 20px; height: 20px; margin: 0 auto 5px;
    border: 1.5px solid var(--copper); border-radius: 50%;
  }
  .brand__name { font-size: 15px; font-weight: 600; color: var(--navy); letter-spacing: .5px; }
  .brand__tagline { font-size: 5.6px; letter-spacing: 1.2px; color: var(--navy); margin-top: 3px; }
  .front-page__band {
    position: absolute; left: 0; right: 0; bottom: 0; height: 148px;
    padding: 30px 16px 0;
    color: var(--white);
    text-align: center;
  }
  .front-page__title {
    font-weight: 800;
    font-size: 14px;
    line-height: 1.35;
    text-transform: uppercase;
    letter-spacing: .3px;
    white-space: nowrap;
  }
  .front-page__web { margin-top: 14px; font-size: 12px; letter-spacing: .5px; }

  /* ---------- inner spread ---------- */
  .inner-shape { position: absolute; inset: 0; }
  .fold { position: absolute; left: 408px; top: 0; width: 1px; height: 100%; background: rgba(0,0,0,.08); }
  .posture-photo {
    position: absolute;
    background: linear-gradient(160deg, var(--mat) 0%, #2a6fb0 45%, #8a2f3a 60%, #3c5ea8 100%);
    border-radius: 2px;
  }
  .intro {
    position: absolute; left: 216px; top: 58px; width: 384px;
    font-size: 7px; line-height: 1.45; text-align: center; color: var(--ink);
  }
  .column { position: absolute; top: 124px; }
  .column--left { left: 152px; width: 238px; }
  .column--right { left: 428px; width: 234px; }
  .posture { margin-bottom: 14px; }
  .posture__tag {
    display: inline-block;
    background: var(--copper);
    color: var(--white);
    font-weight: 700;
    font-size: 8px;
    letter-spacing: .4px;
    padding: 2px 12px 2px 8px;
    border-radius: 0 10px 10px 0;
    margin-bottom: 4px;
  }
  .posture__name { font-weight: 700; font-size: 8px; color: var(--navy); margin-bottom: 2px; }
  .posture__text { font-size: 6.6px; line-height: 1.45; margin-bottom: 3px; }
  .posture__text b { font-weight: 700; }
  .inner-web {
    position: absolute; left: 270px; top: 520px;
    font-size: 7px; font-weight: 600; color: var(--navy);
  }
</style>
</head>
<body>

<section class="spread spread--outer">
  <article class="back-page">
    <h2 class="back-page__title">About the teacher...</h2>
    <p class="back-page__bio">Mara Lindqvist is a current serving Naval Officer, Yoga Therapist (C-YTA) and StillPoint Level 2 instructor. Marisol’s classes are about using the practices and teaching of Yoga to come to the essence of your true self and learning to tap into the internal wisdom which is always present. Mara is dedicated to making the resilience developing practices of Yoga accessible to all Australian Military personnel and their families.</p>

    <p class="quote"><span class="quote__mark">“</span>“Posture should be steady and comfortable”<span class="quote__source">—Yoga Sutras of the sages</span></p>
    <p class="quote"><span class="quote__mark">“</span>“Tension is who you think you are, Relaxation is who you actually are”</p>
    <p class="quote"><span class="quote__mark">“</span>“Life isn’t as serious as the mind makes it out to be”<span class="quote__source">—Oren Vale</span></p>
    <p class="quote"><span class="quote__mark">“</span>“Watch your thoughts, they become words<br>Watch your words, they become actions<br>Watch your actions, they become habits<br>Watch your habits, they become character<br>Watch your character, for it becomes your destiny”<span class="quote__source">—Upanishads</span></p>

    <p class="back-page__web">www.lumaverisk.com.au</p>
  </article>

  <article class="front-page">
    <div class="front-page__photo" role="img" aria-label="Photo of the teacher seated cross-legged in meditation on a blanket in a grassy park with trees"></div>
    <div class="brand">
      <span class="brand__dot"></span>
      <div class="brand__name">Lumavera</div>
      <div class="brand__tagline">Be the change you wish to see in the world</div>
    </div>
    <div class="front-page__band">
      <h1 class="front-page__title">Yoga for Sleep Workshop<br>Restorative Yoga Sleep Sequence</h1>
      <p class="front-page__web">www.lumaverisk.com.au</p>
    </div>
  </article>
</section>

<section class="spread spread--inner">
  <svg class="inner-shape" width="817" height="578" viewBox="0 0 817 578" aria-hidden="true">
    <ellipse cx="408" cy="289" rx="340" ry="318" fill="#f5f4f2"/>
    <ellipse cx="408" cy="289" rx="322" ry="300" fill="none" stroke="#d97c4c" stroke-width="3"/>
  </svg>
  <div class="fold"></div>

  <div class="posture-photo" role="img" aria-label="Posture 1 photo: reclining over a bolster in a T shape with knee support on a blue mat" style="left:22px; top:40px; width:100px; height:215px;"></div>
  <div class="posture-photo" role="img" aria-label="Posture 2 photo: supported bound-angle pose lying back on a bolster" style="left:22px; top:290px; width:100px; height:215px;"></div>
  <div class="posture-photo" role="img" aria-label="Posture 3 photo: elevated legs up the wall with hips on a bolster" style="left:698px; top:40px; width:100px; height:160px;"></div>
  <div class="posture-photo" role="img" aria-label="Posture 4 photo: supported child's pose over a bolster" style="left:698px; top:212px; width:100px; height:150px;"></div>
  <div class="posture-photo" role="img" aria-label="Posture 5 photo: basic relaxation lying on back with pillow under knees" style="left:698px; top:374px; width:100px; height:170px;"></div>

  <p class="intro">Use this sequence to relax and unwind at the end of a day or before bed. Settle comfortably into each posture for about five minutes. Set a timer so you know when it is time to change position, and you can also listen to the audio recording from the Yoga for Sleep Workshop. If you wake in the middle of the night and can’t sleep, you might like to try getting up and resting in any one of these postures for about 5–10 minutes before heading back to bed.</p>

  <div class="column column--left">
    <div class="posture">
      <span class="posture__tag">POSTURE 1 –</span>
      <p class="posture__name">Supported Chest Opening with Knee Support</p>
      <p class="posture__text"><b>PROPS –</b> 2 x bolsters (or towels rolled up lengthways), 1 x cushion for head support (optional)</p>
      <p class="posture__text"><b>SET UP NOTES –</b> Position the props in a T-position with one bolster/towel running parallel to the length of the mat and the other running horizontally under the knees. Position yourself so the parallel bolster runs from the lower back up to behind the head.</p>
      <p class="posture__text"><b>CAUTION –</b> If any lower back pain is experienced adjust the parallel bolster height by using a towel or blanket. Do not use any parallel prop if pain continues.</p>
    </div>
    <div class="posture">
      <span class="posture__tag">POSTURE 2 –</span>
      <p class="posture__name">Supported Bound-Angle Pose</p>
      <p class="posture__text"><b>PROPS –</b> 1 x bolster (or towel rolled up lengthways), 2 x yoga blocks/bolsters (or pillows), 1 x cushion for head support (optional)</p>
      <p class="posture__text"><b>SET UP NOTES –</b> Similar to Posture 1 without the bolster behind the knees. Instead, the soles of the feet come together with knees wide, supported by blocks, bolsters or pillows.</p>
      <p class="posture__text"><b>CAUTION –</b> If any lower back pain is experienced adjust the parallel bolster height using a towel or blanket. Do not use any parallel prop if pain continues.</p>
    </div>
  </div>

  <div class="column column--right">
    <div class="posture">
      <span class="posture__tag">POSTURE 3 –</span>
      <p class="posture__name">Elevated Legs-Up-the-Wall Pose</p>
      <p class="posture__text"><b>PROPS –</b> 1 x bolster (or towel or blanket densely folded to a width of about 15–30cm), 1 x cushion for head support (optional)</p>
      <p class="posture__text"><b>SET UP NOTES –</b> To enter the posture sit with the side of your hip close to the wall, then roll onto your back and extend the legs up the wall. Lift the hips slightly so the bolster can slide underneath the sacrum.</p>
      <p class="posture__text"><b>CAUTION –</b> If any lower back pain is experienced adjust the height the hips are elevated by using a thinner folded towel.</p>
    </div>
    <div class="posture">
      <span class="posture__tag">POSTURE 4 –</span>
      <p class="posture__name">Supported Child’s Pose</p>
      <p class="posture__text"><b>Props –</b> 1–2 x bolsters (or 3–4 bed pillows)</p>
      <p class="posture__text"><b>Set up notes –</b> Position bolster or stacked pillows under torso. Rest the head in one direction and remember to turn to the other side half way through.</p>
      <p class="posture__text"><b>Caution –</b> If any knee or hip pain is experienced, increase the height of the support under the torso.</p>
    </div>
    <div class="posture">
      <span class="posture__tag">POSTURE 5 –</span>
      <p class="posture__name">Basic Relaxation Posture with Knee Support</p>
      <p class="posture__text"><b>Props –</b> 1 x bolster (or 1 x bed pillow or rolled up towel)</p>
      <p class="posture__text"><b>Set up notes –</b> Reclining on back, position bolster or pillows under knees.</p>
    </div>
  </div>

  <p class="inner-web">www.lumaverisk.com.au</p>
</section>

</body>
</html>
```